I need a business card to reflect my new qualifications.
Accredited Teacher, Accredited Valuer & Accredited Judge of Patchwork Quilting.
Fernbrook Lane Studio
47 Harlow Parade, Wodonga Vic 3690
0417 362 958 fernbrook@qlx.com.au

```html
<!DOCTYPE html>
<html lang="en">
<head>
<meta charset="utf-8">
<title>Fernbrook Lane Studio — Business Card</title>
<link rel="stylesheet" href="https://fonts.googleapis.com/css2?family=Courgette&family=Noto+Sans:wght@400&display=swap">
<style>
  :root {
    --card-bg: #fcf5c9;
    --card-bg-edge: #f8efbd;
    --ink-brown: #4b2a0c;
    --title-purple: #7b2e82;
    --title-halo: #f3eefa;
    --stripe-pink: #f77fbe;
    --stripe-cyan: #7ff1f1;
    --stripe-green: #84ec84;
    --stripe-violet: #a07ff0;
    --stripe-orange: #fbb77f;
    --mark-lilac: #e7b7ee;
  }
  html, body {
    margin: 0;
    padding: 0;
    overflow: hidden;
  }
  body {
    width: 1200px;
    height: 823px;
    background: var(--card-bg);
  }
  .card {
    position: relative;
    width: 1200px;
    height: 823px;
    background: radial-gradient(ellipse at center, var(--card-bg) 55%, var(--card-bg-edge) 100%);
    overflow: hidden;
    font-family: "Noto Sans", sans-serif;
    color: var(--ink-brown);
  }
  .studio-mark {
    position: absolute;
    top: 134px;
    left: 0;
    width: 100%;
    display: flex;
    justify-content: center;
    align-items: center;
    gap: 10px;
  }
  .studio-mark__dot {
    width: 14px;
    height: 14px;
    border-radius: 50%;
    background: var(--mark-lilac);
  }
  .studio-mark__name {
    font-size: 20px;
    letter-spacing: 0.5px;
  }
  .studio-title {
    position: absolute;
    top: 310px;
    left: 0;
    width: 100%;
    margin: 0;
    text-align: center;
    font-family: "Courgette", cursive;
    font-weight: 400;
    font-size: 84px;
    line-height: 1;
    color: var(--title-purple);
    text-shadow:
      -2px -2px 0 var(--title-halo),
       2px -2px 0 var(--title-halo),
      -2px  2px 0 var(--title-halo),
       2px  2px 0 var(--title-halo),
       0    3px 4px rgba(80, 40, 90, 0.35);
  }
  .colour-stripe {
    position: absolute;
    top: 440px;
    left: 515px;
    display: flex;
  }
  .colour-stripe span {
    width: 34px;
    height: 13px;
  }
  .colour-stripe .pink   { background: var(--stripe-pink); }
  .colour-stripe .cyan   { background: var(--stripe-cyan); }
  .colour-stripe .green  { background: var(--stripe-green); }
  .colour-stripe .violet { background: var(--stripe-violet); }
  .colour-stripe .orange { background: var(--stripe-orange); }
  .credentials {
    position: absolute;
    top: 536px;
    left: 0;
    width: 100%;
    text-align: center;
  }
  .credentials p {
    margin: 0;
  }
  .credentials__lead,
  .credentials__roles {
    font-size: 48px;
    line-height: 62px;
  }
  .credentials__craft {
    font-size: 38px;
    line-height: 62px;
  }
  .contact {
    position: absolute;
    top: 764px;
    left: 0;
    width: 100%;
    margin: 0;
    text-align: center;
    font-style: normal;
    font-size: 18px;
    line-height: 26px;
  }
  .contact__sep {
    display: inline-block;
    margin: 0 14px;
  }
</style>
</head>
<body>
  <main class="card">
    <div class="studio-mark">
      <span class="studio-mark__dot"></span>
      <span class="studio-mark__name">Fernbrook Lane Studio</span>
    </div>

    <h1 class="studio-title">Fernbrook Lane Studio</h1>

    <div class="colour-stripe" aria-hidden="true">
      <span class="pink"></span><span class="cyan"></span><span class="green"></span><span class="violet"></span><span class="orange"></span>
    </div>

    <section class="credentials">
      <p class="credentials__lead">Accredited</p>
      <p class="credentials__roles">Teacher, Valuer &amp; Judge</p>
      <p class="credentials__craft">of Patchwork Quilting</p>
    </section>

    <address class="contact">
      47 Harlow Parade, Wodonga Vic 3690<span class="contact__sep">·</span>0417 362 958<span class="contact__sep">·</span>fernbrook@qlx.com.au
    </address>
  </main>
</body>
</html>
```